Help Liu Wenhao redesign his business card!

Liu Wenhao, an "influential" Chinese businessman, made international headlines this week with his business card...but not for the right reasons. Help Liu Wenhao redesign his new business card - funny and/or satirical submissions welcome!

Check out his hilarious business card that he was giving out on a trip to New York, with not one, not two...but TEN titles! Let's just say they're not the most humble titles either :).

Read more about Liu's business card here: http://blogs.brightledger.example/asiadesk/2014/01/14/liu-wenhaos-business-card-needs-to-be-recycled/

While the rest of the world is laughing at him, we want to help. This is an unofficial contest, but we'd like the PixelForge community to have a shot at redesigning Liu's business card. Thousands of businesses have used PixelForge.example to create beautiful business cards, so we know the community of designers here can do a great job.

We'd like you to create a business card worthy of this honorable businessman, while also keeping a clean, dignified design.

Funny / satirical job titles and designs are encouraged. Note you do not have to use all of Liu's titles on the card. Feel free to come up with your own creative titles!

In regard to contact details, please use dummy contact details. Liu's company name and street address are:

China Tai-Mo Reusable Scrap & Restoration Corporation
Fuxing Road 7, Lanqiao District, Nanjing, China

You can design a single sided or double-sided card - it's completely up to you!

Target Market(s)

Business people and government officials of the world

Industry/Entity Type

Business

Font styles to use
Serif
Sans Serif
Decorative

Colors
ec2027
ffc214
6b449b
0455a3

Requirements
Must have
• At least 1 title, preferably more than 1.

Designers can approach this task how they like however one option could be to use one of Liu's titles and create a suitable business card graphic to suit the role. Designers are also encouraged to o make up a new title and design a graphic to suit.

Here are the titles - but you can also make up your own!

Most influential person of China
Most prominent Philanthropist of China
China Moral Leader
China Earthquake Rescue Hero
Most well-known and Beloved Chinese Role Model
China Top Ten Most Honorable Volunteer
Most Charismatic Philanthropist of China
China Low Carbon Emission
Environmental Protection Top Advocate
China's Foremost Environmental Preservation Demolition Expert
Should not have
• No black borders around photographs of Liu Wenhao
Do not present Liu Wenhao's image in grayscale (black and white)

For a detailed guideline for colors to avoid in design targeting the Chinese market, see http://www.corvalegroup.example/2011/01/17/color/

```html
<!DOCTYPE html>
<html lang="en">
<head>
<meta charset="utf-8">
<title>Wenhao Liu – Business Card</title>
<link href="https://fonts.googleapis.com/css2?family=Cinzel:wght@500;600;700&display=swap" rel="stylesheet">
<style>
  :root {
    --page: #ffffff;
    --card-dark: #0c0c0c;
    --card-mid: #2a2a2a;
    --ink: #ffffff;
    --brand-red: #ec2027;
    --brand-yellow: #ffc214;
    --brand-purple: #6b449b;
    --brand-blue: #0455a3;
    --portrait-warm: #8a7a68;
    --portrait-deep: #3b2a22;
  }
  html, body {
    margin: 0;
    padding: 0;
    width: 1147px;
    height: 1200px;
    overflow: hidden;
    background: var(--page);
  }
  .canvas {
    position: relative;
    width: 1147px;
    height: 1200px;
    font-family: "Cinzel", "Times New Roman", serif;
    color: var(--ink);
  }
  .card {
    position: absolute;
    left: 116px;
    width: 924px;
    height: 511px;
    overflow: hidden;
    background: linear-gradient(135deg, var(--card-mid) 0%, var(--card-dark) 45%, var(--card-mid) 75%, var(--card-dark) 100%);
  }
  .card--front { top: 66px; }
  .card--back { top: 633px; }

  .portrait {
    position: absolute;
    left: 37px;
    top: 0;
    width: 343px;
    height: 511px;
    background: linear-gradient(160deg, var(--portrait-warm) 0%, #6d5d4e 45%, var(--portrait-deep) 100%);
  }

  .dot {
    position: absolute;
    width: 14px;
    height: 14px;
    border-radius: 50%;
    background: var(--ink);
  }
  .front-dot { left: 647px; top: 66px; }

  .rule {
    position: absolute;
    left: 510px;
    width: 287px;
    height: 2px;
    background: linear-gradient(90deg, var(--brand-red), var(--brand-yellow) 33%, var(--brand-purple) 66%, var(--brand-blue));
  }
  .rule--top { top: 114px; }
  .rule--bottom { top: 192px; }

  .name {
    position: absolute;
    left: 380px;
    width: 548px;
    top: 126px;
    margin: 0;
    text-align: center;
    font-size: 44px;
    font-weight: 600;
    letter-spacing: 1px;
    text-transform: uppercase;
  }
  .role {
    position: absolute;
    left: 380px;
    width: 548px;
    top: 209px;
    margin: 0;
    text-align: center;
    font-size: 24px;
    font-weight: 600;
  }
  .company {
    position: absolute;
    left: 380px;
    width: 548px;
    top: 448px;
    margin: 0;
    text-align: center;
    font-size: 15.5px;
    font-weight: 700;
    line-height: 19px;
  }

  .back-dot--top { left: 455px; top: 50px; }
  .back-dot--bottom { left: 455px; top: 443px; }
  .titles {
    position: absolute;
    left: 0;
    right: 0;
    top: 76px;
    margin: 0;
    padding: 0;
    list-style: none;
    text-align: center;
    font-size: 23px;
    font-weight: 700;
    line-height: 36.4px;
  }
</style>
</head>
<body>
<div class="canvas">
  <section class="card card--front">
    <div class="portrait" role="img" aria-label="Portrait of Wenhao Liu in a dark suit seated at a wooden desk"></div>
    <span class="dot front-dot"></span>
    <span class="rule rule--top"></span>
    <h1 class="name">Wenhao Liu</h1>
    <span class="rule rule--bottom"></span>
    <p class="role">CEO</p>
    <p class="company">China Tai-Mo Reusable Scrap &amp; Restoration Corporation<br>Fuxing Road 7, Lanqiao District, Nanjing, China</p>
  </section>

  <section class="card card--back">
    <span class="dot back-dot--top"></span>
    <ul class="titles">
      <li>Most influential person of China</li>
      <li>Most prominent Philanthropist of China</li>
      <li>China Moral Leader</li>
      <li>China Earthquake Rescue Hero</li>
      <li>Most well-known and Beloved Chinese Role Model</li>
      <li>China Top Ten Most Honorable Volunteer</li>
      <li>Most Charismatic Philanthropist of China</li>
      <li>China Low Carbon Emission</li>
      <li>Environmental Protection Top Advocate</li>
      <li>China’s Foremost Environmental Preservation Demolition Expert</li>
    </ul>
    <span class="dot back-dot--bottom"></span>
  </section>
</div>
</body>
</html>
```